Face Mask Box

We need a box design for medical face masks, with our brand logo and emphasizing that the product is made in the USA, so maybe more than just a made in USA icon maybe the packaging should be red/white/blue or a flag etc... would like an image of the product (which we can substitute later) or the product being worn, maybe a rendering as well. Icons for all of its features (we can put those on later), a place for the UPC. We can put text on later, looking for the base graphic design right now.

```html
<!DOCTYPE html>
<html lang="en">
<head>
<meta charset="utf-8">
<title>Face Mask Box – Dieline</title>
<link rel="stylesheet" href="https://fonts.googleapis.com/css2?family=Montserrat:wght@700;800;900&family=Roboto:wght@400;500&display=swap">
<style>
  :root{
    --navy:#262f7e;
    --cut:#e3262a;
    --fold:#f08a7a;
    --red:#e3261f;
    --blue:#1d78cc;
    --sky:#8cc4ea;
    --orange:#f39a2c;
    --white:#ffffff;
  }
  html,body{margin:0;padding:0;overflow:hidden;background:var(--white);}
  .dieline{position:relative;width:1200px;height:436px;overflow:hidden;background:var(--white);font-family:"Roboto",sans-serif;}
  .guides{position:absolute;inset:0;width:1200px;height:436px;}
  .panel{position:absolute;overflow:hidden;}
  .backdrop{position:absolute;inset:0;
    background:
      radial-gradient(ellipse 55% 45% at 45% 0%, rgba(255,255,255,.95), rgba(255,255,255,0) 70%),
      radial-gradient(ellipse 70% 40% at 40% 30%, rgba(255,255,255,.8), rgba(255,255,255,0) 70%),
      linear-gradient(105deg, var(--blue) 0%, var(--sky) 35%, #f4eeee 58%, #f07a62 78%, var(--red) 100%);}
  .panel--front{left:19px;top:191px;width:481px;height:215px;}
  .panel--lid{left:708px;top:19px;width:475px;height:172px;transform:rotate(180deg);}
  .panel--back{left:702px;top:191px;width:484px;height:219px;}
  .panel--back .backdrop{background:
      radial-gradient(ellipse 45% 40% at 50% 40%, rgba(255,255,255,.95), rgba(255,255,255,0) 70%),
      linear-gradient(110deg, var(--blue) 0%, var(--sky) 35%, #f6f2f2 58%, #f07a62 80%, var(--red) 100%);}
  .product-shot{position:absolute;border-radius:40% 40% 48% 48% / 20% 20% 60% 60%;
    background:linear-gradient(180deg,#d9f0f6,#a9dbe8 60%,#c6e9f1);}
  .brand{position:absolute;display:flex;align-items:center;gap:4px;font-family:"Montserrat",sans-serif;font-weight:700;color:var(--navy);font-size:10px;letter-spacing:.3px;}
  .brand-dot{width:8px;height:8px;border-radius:50%;background:var(--orange);}
  .count-badge{position:absolute;border-radius:50%;background:var(--navy);border:3px solid var(--orange);box-shadow:0 0 0 2px var(--white);
    display:flex;flex-direction:column;align-items:center;justify-content:center;color:var(--white);font-family:"Montserrat",sans-serif;}
  .count-badge .num{font-weight:900;line-height:1;}
  .count-badge .label{background:var(--orange);font-weight:800;padding:1px 3px;margin-top:1px;white-space:nowrap;}
  .origin{position:absolute;display:flex;flex-direction:column;align-items:center;font-family:"Montserrat",sans-serif;font-weight:800;color:var(--red);line-height:1;text-align:center;}
  .origin-shield{background:linear-gradient(180deg,var(--navy) 0 30%,var(--red) 30%);clip-path:polygon(0 0,100% 0,100% 70%,50% 100%,0 70%);margin-top:2px;}
  .title{position:absolute;font-family:"Montserrat",sans-serif;font-weight:900;color:var(--navy);margin:0;white-space:nowrap;letter-spacing:.2px;}
  .subtitle{position:absolute;font-family:"Roboto",sans-serif;color:var(--navy);margin:0;white-space:nowrap;}
  .window{position:absolute;left:89px;top:34px;width:307px;height:146px;border:1px solid var(--cut);border-radius:14px;}
</style>
</head>
<body>
<div class="dieline">
  <svg class="guides" viewBox="0 0 1200 436" aria-hidden="true">
    <g fill="none" stroke-width="0.8">
      <path stroke="var(--cut)" d="M0 19H19L50 0M470 0L500 19H22V191 M500 19H704L680 0 M708 0V19H1183V0"/>
      <path stroke="var(--fold)" d="M22 19V191 M494 19V191 M0 191H1200 M0 291H19 M500 291H702 M1186 291H1200"/>
      <path stroke="var(--cut)" d="M211 401L218 418Q220 424 226 424H292Q298 424 300 418L307 401"/>
      <path stroke="var(--cut)" d="M708 410V422Q708 432 720 432H1168Q1180 432 1180 422V410 M1183 0V191"/>
      <path stroke="var(--fold)" d="M19 406H500M702 410H1186"/>
    </g>
  </svg>

  <section class="panel panel--front">
    <div class="backdrop" role="img" aria-label="Red, white and blue star-pattern wave backdrop"></div>
    <div class="product-shot" role="img" aria-label="Pleated blue disposable face mask with ear loops" style="left:125px;top:41px;width:232px;height:125px;"></div>
    <div class="origin" style="left:25px;top:10px;font-size:5.5px;">PROUDLY<br>MADE IN USA
      <div class="origin-shield" style="width:32px;height:40px;"></div></div>
    <div class="brand" style="left:212px;top:25px;"><span class="brand-dot"></span>SHIELDWELL</div>
    <div class="count-badge" style="left:413px;top:10px;width:48px;height:48px;">
      <span class="num" style="font-size:17px;">50</span><span class="label" style="font-size:6px;">PCS INSIDE</span></div>
    <h1 class="title" style="left:64px;top:164px;font-size:25px;">DISPOSABLE FACE MASK</h1>
    <p class="subtitle" style="left:337px;top:191px;font-size:13px;">(Non-medical)</p>
  </section>

  <section class="panel panel--lid">
    <div class="backdrop" role="img" aria-label="Red, white and blue star-pattern wave backdrop"></div>
    <div class="product-shot" role="img" aria-label="Pleated blue disposable face mask with ear loops" style="left:4px;top:10px;width:180px;height:110px;"></div>
    <div class="brand" style="left:195px;top:28px;"><span class="brand-dot"></span>SHIELDWELL</div>
    <div class="origin" style="left:420px;top:12px;font-size:5px;">PROUDLY<br>MADE IN USA
      <div class="origin-shield" style="width:30px;height:36px;"></div></div>
    <div class="count-badge" style="left:413px;top:72px;width:46px;height:46px;">
      <span class="num" style="font-size:16px;">50</span><span class="label" style="font-size:5.5px;">PCS INSIDE</span></div>
    <h2 class="title" style="left:60px;top:122px;font-size:24px;">DISPOSABLE FACE MASK</h2>
    <p class="subtitle" style="left:260px;top:148px;font-size:12px;">(Non-medical)</p>
  </section>

  <section class="panel panel--back">
    <div class="backdrop" role="img" aria-label="Red, white and blue star-pattern wave backdrop"></div>
    <div class="window" aria-label="Dispensing window"></div>
  </section>
</div>
</body>
</html>
```